Bold, Modern, Clean "Quarvenstretch.com" website

Why we stand out?
We are a male and female mobile massage team. Our names are Todd and Lise. 
Quarven Tide is a Seattle based mobile massage service. Our massage is offered to the community with a goal of facilitating balance within each individual. We specialize in integrated Pain management, and sports/medical massage therapy. Every client's first assessment is attended by our male and female massage therapist team. Depending on the goals identified for an individual determines which therapist will be assigned to provide treatment, if not both.

Our passion...
Here at Quarven Tide, we have a great passion for Postural Resoration and how it is integrated into an individual's Massage treatment. We pride ourselves in being natural facilitators of healing, which takes the ego of the therapist out of the client's healing process. We strive to deliver the best massage possible by including modalities such as Neuromuscular, Myofascial release, spontaneous muscle release, postural restoration, orthopedic, and medical massage.

Our education...

We are both Graduates of Halvenor, school of massage therapy. We have continuing education in medical massage, myofacial release, trigger point therapy, postural restoration, anatomy, and spontaneous muscle release. Lise is also a Certified Yoga Instructor, which amplifies her experience with flexibility and strength as it pertains to each individual. Todd's passion is Massage, stretching, and strength training to encourage postural restoration and realignment.

Our rates-

Our rates are $75/ 60 minutes, $95/ 90 minutes, and $120/ 120 minutes.

Education-
Both Lise and I worked as behavioral health professionals that specialized in life skills mentoring for youth who had experienced different types of trauma. This led us both to want to help others in a different environment, where individuals can be empowered to take responsibility over their own healing. To us, massage is a type of manipulation physical therapy, that encourages healing on many levels.

Advice to any massage client-
The most important thing to 'us', as Licenced providers is to get you on to our table to show you our skills. But a good therapist never forgets that it's not about what we do for you, but what we can facilitate for you. Your health and healing has nothing to do with us. It is yours, not ours. Identify what your goals are with any Therapist, and know what the end looks like. Progress should be tangible, such as range of motion, and decreased pain.

5/5 stars Massage Therapy
Verified Review

Lise and Todd at Quarven Tide are awesome! I recently had open heart surgery, and Lise worked on me to increase my range of motion while helping with the pinched nerve from my arm being in the same position for so long during my surgery. My wife drives a lot for work, and Todd has helped decrease her neck and lower back pain immensely. They are seriously the best therapists I have ever worked with. I would recommend them to anyone who needs anything from stress relief to a medical massage treatment. They are professional, up beat, easy going, and always on time. And, I love that they meet us where ever we like! We did a staycation recently, where they came to our hotel to give us relaxation massages. Although usually they come to our home, where we focus on pain related issues. We will continue to work with them for a long, long time.

Bressa K. on December 17, 2015

Target Market(s)

Mobile massage therapy clients

Industry/Entity Type

Massage Therapy

Font styles to use
Serif
Sans Serif

Requirements
Must have
• Please add or remove any information that would help the presentation of our website. Our logo is posted below, please include into the website.
• Please include a contact field that includes, quarvenstretch@mailbrook.net,
• (206) 555-0194
• We have also included our own stock photos, as well as a photo of Todd and Lise. Please include a cropped photo of both massage therapists.

```html
<!DOCTYPE html>
<html lang="en">
<head>
<meta charset="utf-8">
<title>Quarven Tide Mobile Massage</title>
<link rel="stylesheet" href="https://fonts.googleapis.com/css2?family=Raleway:wght@400;500;600;700&family=Lobster&family=Kaushan+Script&display=swap">
<style>
:root{
  --cyan:#14c4d4;
  --teal:#0b8e94;
  --ink:#222222;
  --text:#555555;
  --muted:#888888;
  --nav:#161616;
  --page:#f7f7f7;
  --white:#ffffff;
  --field:#d6d6d6;
  --logo-blue:#1b3fa8;
}
*{box-sizing:border-box;margin:0;padding:0}
html,body{width:1200px;height:2200px;overflow:hidden;background:var(--page)}
body{font-family:"Raleway",Arial,sans-serif;color:var(--text);position:relative}
.abs{position:absolute}

/* header */
.topbar{left:0;top:0;width:1200px;height:76px;background:var(--white)}
.contact-line{right:138px;font-size:15px;color:var(--ink);display:flex;align-items:center;gap:8px}
.contact-line.phone{top:10px}
.contact-line.mail{top:45px;font-size:16px}
.mainnav{left:0;top:76px;width:1200px;height:47px;background:var(--nav);border-bottom:3px solid var(--cyan)}
.mainnav ul{list-style:none;position:absolute;left:348px;top:0;display:flex;height:44px}
.mainnav li{color:var(--white);font-size:15px;padding:0 24px;line-height:44px;border-left:1px solid #333;position:relative}
.mainnav li:first-child{border-left:none}
.mainnav li.active::after{content:"";position:absolute;left:50%;bottom:0;margin-left:-7px;border:7px solid transparent;border-bottom-color:var(--cyan)}
.brand-box{left:142px;top:0;width:152px;height:160px;background:var(--white);box-shadow:0 2px 6px rgba(0,0,0,.2);z-index:3}
.brand{left:7px;top:7px;width:138px;height:138px;border-radius:50%;background:var(--logo-blue);border:4px solid var(--white);outline:3px solid var(--logo-blue);display:flex;align-items:center;justify-content:center;text-align:center;color:var(--white);font-weight:700;font-size:21px;line-height:1.05}

/* hero */
.hero-photo{left:0;top:123px;width:1200px;height:452px;background:radial-gradient(ellipse at 62% 55%,#c98f6c 0%,#9b6547 28%,#3d6b1e 55%,#1f4a10 100%)}
.hero-title{left:160px;top:218px;font-family:"Lobster",cursive;color:var(--white);font-size:56px;line-height:1.1;text-shadow:0 2px 4px rgba(0,0,0,.4)}
.hero-title span{display:block}
.hero-title span+span{padding-left:70px}
.hero-rule{left:165px;top:353px;width:220px;height:1px;background:rgba(255,255,255,.8)}
.hero-tag{left:200px;top:366px;font-family:"Kaushan Script",cursive;color:var(--white);font-size:24px}
.slide-arrow{top:325px;width:38px;height:38px;border-radius:50%;background:rgba(255,255,255,.55);display:flex;align-items:center;justify-content:center}

/* inquiry */
.inquiry{left:744px;top:512px;width:320px;height:500px;background:var(--white);border-radius:10px 10px 0 0;box-shadow:0 0 8px rgba(0,0,0,.12);padding:0 22px;text-align:center}
.inquiry h2{font-weight:400;font-size:29px;color:var(--ink);margin-top:13px}
.inquiry .lead{font-size:11.5px;font-weight:600;color:var(--ink);margin-top:4px}
.field{height:32px;border:1px solid var(--field);border-radius:3px;margin-top:11px;text-align:left;font-size:12px;color:var(--muted);padding:8px 16px;position:relative}
.field:first-of-type{margin-top:16px}
.field.select .caret{position:absolute;right:12px;top:8px;width:16px;height:14px;border:1px solid #999;background:#eee}
.field.area{height:120px}
.cta{margin-top:22px;height:44px;border-radius:5px;background:var(--cyan);color:var(--white);font-weight:700;font-size:16px;line-height:44px}
.privacy{margin-top:12px;font-size:10.5px;color:var(--muted);font-weight:600}

/* about */
.about-title{left:139px;top:592px;font-size:38px;font-weight:400;color:var(--ink)}
.about-rule{left:139px;top:655px;width:558px;height:1px;background:#444}
.about-copy{left:139px;top:678px;width:545px;font-size:15px;line-height:24px}
.feature{left:139px;display:flex;gap:14px}
.feature .icon{width:36px;height:36px;border-radius:50%;background:var(--cyan);flex:none;display:flex;align-items:center;justify-content:center}
.feature h3{font-size:18px;font-weight:600;color:var(--ink);margin-top:-2px}
.feature p{font-size:13.5px;margin-top:2px}
.feature p b{color:var(--ink);text-decoration:underline;font-weight:700}
.view-all{left:540px;top:1025px;width:120px;height:34px;background:var(--cyan);color:var(--white);font-weight:700;font-size:15px;text-align:center;line-height:34px}

/* prices */
.prices{left:0;top:1085px;width:1200px;height:404px;background:var(--teal)}
.section-title{width:1200px;left:0;text-align:center;font-weight:400;font-size:38px}
.prices .section-title{top:20px;color:var(--white)}
.prices-rule{left:461px;top:83px;width:278px;height:1px;background:rgba(255,255,255,.8)}
.price-card{top:113px;width:291px;height:235px;background:var(--white);border-radius:18px;text-align:center;padding:22px 18px 0}
.price-card h3{font-size:32px;font-weight:700;color:var(--ink)}
.price-card h3 sup{font-size:15px}
.price-card .rate{font-size:19px;color:var(--ink);margin-top:6px;padding-bottom:10px;border-bottom:1px solid #444}
.price-card .rate sup{font-size:11px}
.price-card h4{font-weight:400;font-size:18px;color:var(--ink);margin-top:18px}
.price-card p{font-size:12.5px;line-height:17px;margin-top:6px}
.badge{top:324px;width:66px;height:66px;margin-left:-33px;border-radius:50%;background:var(--white);display:flex;align-items:center;justify-content:center}
.badge span{width:32px;height:32px;border-radius:50%;background:#262626;color:var(--white);font-weight:700;font-size:16px;line-height:32px;text-align:center}

/* testimonial */
.testi .section-title{top:1510px;color:var(--ink)}
.testi-rule{left:415px;top:1581px;width:370px;height:1px;background:#444}
.testi-accent{left:556px;top:1580px;width:88px;height:3px;background:var(--cyan)}
.avatar{left:151px;top:1593px;width:152px;height:152px;border-radius:50%;border:7px solid var(--cyan);background:linear-gradient(160deg,#5a4a42,#1e1a1a)}
.client-name{left:326px;top:1607px;font-size:28px;font-weight:600;color:var(--ink)}
.client-role{left:326px;top:1645px;font-size:16px}
.quote{left:326px;top:1670px;width:730px;font-size:16px;line-height:24px}
.dots{left:574px;top:1764px;display:flex;gap:6px}
.dots i{width:14px;height:14px;border-radius:50%;border:2px solid var(--cyan)}
.dots i.on{background:var(--teal);border-color:var(--cyan)}

/* footer */
.footer-line{left:0;top:1834px;width:1200px;height:6px;background:var(--cyan)}
.footer{left:0;top:1840px;width:1200px;height:360px;background:linear-gradient(90deg,#5a4538 0%,#3b2c23 45%,#4a362a 70%,#2c211b 100%)}
.foot-brand{left:553px;top:1863px;width:96px;height:96px;border-radius:50%;background:var(--logo-blue);border:3px solid var(--white);color:var(--white);font-weight:700;font-size:14px;line-height:1.05;display:flex;align-items:center;justify-content:center;text-align:center}
.foot-nav{left:0;top:1975px;width:1200px;display:flex;justify-content:center;gap:52px;list-style:none;font-size:13px;color:var(--white)}
.foot-rule{height:1px;background:rgba(255,255,255,.7)}
.foot-phone{left:0;top:2027px;width:1200px;display:flex;justify-content:center;align-items:center;gap:10px;color:var(--cyan);font-weight:700;font-size:30px}
.social{left:536px;top:2106px;display:flex;gap:6px}
.social i{width:28px;height:28px;border-radius:50%;background:var(--white)}
.copyright{left:0;top:2150px;width:1200px;text-align:center;font-size:11px;color:var(--white)}
</style>
</head>
<body>

<header>
  <div class="abs topbar"></div>
  <div class="abs contact-line phone">
    <svg width="16" height="16" viewBox="0 0 24 24"><path fill="#14c4d4" d="M6.6 10.8a15.1 15.1 0 0 0 6.6 6.6l2.2-2.2c.3-.3.7-.4 1-.2 1.1.4 2.3.6 3.6.6.6 0 1 .4 1 1V20c0 .6-.4 1-1 1A17 17 0 0 1 3 4c0-.6.4-1 1-1h3.5c.6 0 1 .4 1 1 0 1.3.2 2.5.6 3.6.1.3 0 .7-.2 1z"/></svg>
    (206) 555-0194
  </div>
  <div class="abs contact-line mail">
    <svg width="20" height="14" viewBox="0 0 20 14"><rect width="20" height="14" rx="1" fill="#14c4d4"/><path d="M1 1l9 7 9-7" stroke="#fff" stroke-width="1.5" fill="none"/></svg>
    quarvenstretch@mailbrook.net
  </div>
  <nav class="abs mainnav">
    <ul>
      <li class="active">Home</li><li>About Us</li><li>Services</li><li>Education</li><li>Photo Gallery</li><li>Prices</li><li>Contact</li>
    </ul>
  </nav>
  <div class="abs brand-box"><div class="abs brand">Quarven<br>Tide</div></div>
</header>

<section class="hero">
  <div class="abs hero-photo" role="img" aria-label="Woman relaxing face down receiving a herbal compress massage, flower in hair, candles and green foliage behind"></div>
  <h1 class="abs hero-title"><span>Massage</span><span>Therapy</span></h1>
  <div class="abs hero-rule"></div>
  <p class="abs hero-tag">We Come To You</p>
  <div class="abs slide-arrow" style="left:53px"><svg width="12" height="14" viewBox="0 0 12 14"><path d="M9 1L3 7l6 6" stroke="#555" stroke-width="1.6" fill="none"/></svg></div>
  <div class="abs slide-arrow" style="left:1108px"><svg width="12" height="14" viewBox="0 0 12 14"><path d="M3 1l6 6-6 6" stroke="#555" stroke-width="1.6" fill="none"/></svg></div>
</section>

<form class="abs inquiry">
  <h2>Quick Inquiry</h2>
  <p class="lead">Fill out the form below for your Inquiry.</p>
  <div class="field">Full Name</div>
  <div class="field">Email Address</div>
  <div class="field">Phone Number</div>
  <div class="field select">Type of Massage Therapy<span class="caret"></span></div>
  <div class="field area">Briefly Describe Your Massage</div>
  <div class="cta">GET STARTED NOW</div>
  <p class="privacy">&#128274; Your information will never be shared</p>
</form>

<section class="about">
  <h2 class="abs about-title">About Us</h2>
  <div class="abs about-rule"></div>
  <p class="abs about-copy">Quarven Tide is a Seattle based mobile massage service. Our massage is offered to the community with a goal of facilitating balance within each individual. We specialize in integrated Pain management, and sports/medical massage therapy.</p>
  <div class="abs feature" style="top:795px">
    <div class="icon"><svg width="18" height="18" viewBox="0 0 18 18"><circle cx="9" cy="4" r="3" fill="#fff"/><path d="M3 16c0-4 3-6 6-6s6 2 6 6" fill="#fff"/></svg></div>
    <div><h3>Why we stand out?</h3><p>We are a male and female mobile massage team. <b>+More.</b></p></div>
  </div>
  <div class="abs feature" style="top:867px">
    <div class="icon"><svg width="18" height="18" viewBox="0 0 18 18"><path d="M9 16S2 11 2 6.5A3.5 3.5 0 0 1 9 5a3.5 3.5 0 0 1 7 1.5C16 11 9 16 9 16z" fill="#fff"/></svg></div>
    <div><h3>Our Passion...</h3><p>Here at Quarven Tide, we have a great passion for Postural Resoration. <b>+More.</b></p></div>
  </div>
  <div class="abs feature" style="top:938px">
    <div class="icon"><svg width="20" height="16" viewBox="0 0 20 16"><path d="M10 1L1 6l9 5 9-5z" fill="#fff"/><path d="M5 8.5V12c0 1.5 2.5 3 5 3s5-1.5 5-3V8.5L10 11z" fill="#fff"/></svg></div>
    <div><h3>Our Education...</h3><p>We are both Graduates of Halvenor, school of massage therapy. <b>+More.</b></p></div>
  </div>
  <div class="abs view-all">VIEW ALL</div>
</section>

<section class="abs prices">
  <h2 class="abs section-title">Our Prices</h2>
  <div class="abs prices-rule"></div>
  <article class="abs price-card" style="left:144px">
    <h3>1-hour</h3><p class="rate">$75 Introductory Price<sup>*</sup></p>
    <h4>Essential therapeutic relief</h4>
    <p>Donec porta nulla nec portitor ornare. Quisque vulputate. Duis eu sollicitudin elit.Fusce hendrerit orci eu elit commodo. ut feugiat</p>
  </article>
  <article class="abs price-card" style="left:455px">
    <h3>1<sup>½</sup>-hour</h3><p class="rate">$95 Introductory Price<sup>*</sup></p>
    <h4>Complete therapeutic relief</h4>
    <p>Donec porta nulla nec portitor ornare. Quisque vulputate. Duis eu sollicitudin elit.Fusce hendrerit orci eu elit commodo. ut feugiat</p>
  </article>
  <article class="abs price-card" style="left:764px">
    <h3>2-hour</h3><p class="rate">$120 Introductory Price<sup>*</sup></p>
    <h4>Maximum therapeutic relief</h4>
    <p>Donec porta nulla nec portitor ornare. Quisque vulputate. Duis eu sollicitudin elit.Fusce hendrerit orci eu elit commodo. ut feugiat</p>
  </article>
  <div class="abs badge" style="left:289px"><span>1</span></div>
  <div class="abs badge" style="left:600px"><span>2</span></div>
  <div class="abs badge" style="left:910px"><span>3</span></div>
</section>

<section class="testi">
  <h2 class="abs section-title">What Client Say About US</h2>
  <div class="abs testi-rule"></div>
  <div class="abs testi-accent"></div>
  <div class="abs avatar" role="img" aria-label="Portrait photo of the client"></div>
  <h3 class="abs client-name">Dorian Vale</h3>
  <p class="abs client-role">Family Law</p>
  <p class="abs quote">The most important thing to 'us', as Licenced providers is to get you on to our table to show you our skills. But a good therapist never forgets that it's not about what we do for you, but what we can facilitate for you.</p>
  <div class="abs dots"><i class="on"></i><i></i><i></i></div>
</section>

<footer>
  <div class="abs footer-line"></div>
  <div class="abs footer" role="img" aria-label="Dimmed spa background with a man receiving a massage and candles"></div>
  <div class="abs foot-brand">Quarven<br>Tide</div>
  <ul class="abs foot-nav"><li>HOME</li><li>ABOUT US</li><li>SERVICES</li><li>PHOTO GALLERY</li><li>EDUCATION</li><li>PRICES</li><li>CONTACT</li></ul>
  <div class="abs foot-rule" style="left:384px;top:2019px;width:433px"></div>
  <div class="abs foot-phone">
    <svg width="30" height="30" viewBox="0 0 24 24"><path fill="#cccccc" d="M6.6 10.8a15.1 15.1 0 0 0 6.6 6.6l2.2-2.2c.3-.3.7-.4 1-.2 1.1.4 2.3.6 3.6.6.6 0 1 .4 1 1V20c0 .6-.4 1-1 1A17 17 0 0 1 3 4c0-.6.4-1 1-1h3.5c.6 0 1 .4 1 1 0 1.3.2 2.5.6 3.6.1.3 0 .7-.2 1z"/></svg>
    (206) 555-0194
  </div>
  <div class="abs foot-rule" style="left:415px;top:2083px;width:370px"></div>
  <div class="abs social"><i></i><i></i><i></i><i></i></div>
  <p class="abs copyright">Copyright © 2015 Quarven Tide.</p>
</footer>

</body>
</html>
```